Redesign Business Cards, Attached

Please read instructions carefully. If you have any questions send a message before submitting your ONE design. Please redesign attached business cards. Double sided. Use same content and descriptions. Use black, silver, crimson red and gold colors. My only issue with the attached design is the background colors. I like the layout as-is. I can provide the individual pictures on the back side later. Do not submit more than one design. One submission shall include both front and back. Do not submit front and back separately. A second project will be launched to create a matching post card after completion of this.
Industry/Entity Type
see description and attachments.
Contact Information for Business Card
Requirements
Must have
- see description and attachments.
Nice to have
Should not have

```html
<!DOCTYPE html>
<html lang="en">
<head>
<meta charset="utf-8">
<title>Harbor Helm Boat Training – Business Card</title>
<link href="https://fonts.googleapis.com/css2?family=Montserrat:wght@300;400;500;600&family=Oswald:wght@400&display=swap" rel="stylesheet">
<style>
  :root {
    --backdrop: #e6e7e8;
    --card: #ffffff;
    --black: #141414;
    --charcoal: #2b2b2d;
    --crimson: #a4182e;
    --crimson-deep: #6e0f1e;
    --gold: #c9a233;
    --silver: #939598;
    --silver-light: #c8cacd;
    --ink: #111111;
    --muted: #8a8c8f;
  }
  * { box-sizing: border-box; margin: 0; padding: 0; }
  html, body { width: 1200px; height: 1163px; overflow: hidden; }
  body {
    background: var(--backdrop);
    position: relative;
    font-family: "Montserrat", sans-serif;
  }
  .card {
    position: absolute;
    width: 724px;
    height: 414px;
    background: var(--card);
    overflow: hidden;
    box-shadow: 6px 8px 10px rgba(0,0,0,0.28);
  }
  .card--front { left: 256px; top: 119px; }
  .card--back { left: 254px; top: 577px; height: 415px; }

  .card--front .sea-photo {
    position: absolute;
    left: 0; top: 0; width: 330px; height: 414px;
    background: linear-gradient(160deg, var(--charcoal) 0%, var(--black) 45%, var(--crimson-deep) 100%);
    clip-path: polygon(0 0, 329px 0, 257px 205px, 329px 414px, 0 414px);
  }
  .brand-disc {
    position: absolute;
    border-radius: 50%;
    background: var(--card);
    display: flex;
    align-items: center;
    justify-content: center;
    text-align: center;
    color: var(--ink);
    font-weight: 600;
    text-transform: uppercase;
  }
  .card--front .brand-disc {
    left: 104px; top: 102px; width: 220px; height: 220px;
    font-size: 18px; line-height: 1.3; letter-spacing: 1px;
  }
  .holder-name {
    position: absolute; left: 362px; top: 82px;
    font-size: 29px; font-weight: 500; color: var(--ink); letter-spacing: 0.3px;
    white-space: nowrap;
  }
  .holder-title {
    position: absolute; left: 362px; top: 124px;
    font-size: 23px; font-weight: 300; color: var(--muted); line-height: 28px;
  }
  .phone-pill {
    position: absolute; left: 366px; top: 212px; width: 277px; height: 51px;
    border-radius: 25px; background: var(--crimson);
    display: flex; align-items: center; justify-content: center;
    font-size: 25px; font-weight: 400; color: var(--card);
  }
  .contact-line {
    position: absolute; left: 362px;
    font-size: 23px; font-weight: 300; color: var(--muted);
  }
  .contact-line--email { top: 300px; }
  .contact-line--web { top: 336px; }

  .back-band {
    position: absolute; left: 0; top: 0; width: 724px; height: 163px;
    background: var(--black);
    border-bottom: 4px solid var(--gold);
  }
  .card--back .sea-photo {
    position: absolute;
    left: 500px; top: 0; width: 224px; height: 163px;
    background: linear-gradient(200deg, var(--silver-light) 0%, var(--silver) 45%, var(--crimson-deep) 100%);
    clip-path: polygon(82px 0, 224px 0, 224px 163px, 88px 163px, 1px 81px);
  }
  .card--back .brand-disc {
    left: 45px; top: 21px; width: 124px; height: 124px;
    font-size: 11px; line-height: 1.3;
  }
  .band-web {
    position: absolute; left: 193px; top: 63px;
    font-size: 26px; font-weight: 400; color: var(--gold);
  }
  .service-grid {
    position: absolute; left: 41px; top: 191px;
    display: grid;
    grid-template-columns: repeat(4, 157px);
    grid-template-rows: repeat(2, 98px);
    column-gap: 5px; row-gap: 6px;
    list-style: none;
  }
  .service {
    display: flex; align-items: center; justify-content: center; text-align: center;
    font-family: "Oswald", sans-serif; font-size: 20px; line-height: 22px;
    color: var(--card); text-transform: uppercase;
    padding: 0 8px;
  }
  .service--silver { background: var(--silver); }
  .service--accent { background: var(--crimson); }
</style>
</head>
<body>
  <section class="card card--front">
    <div class="sea-photo" role="img" aria-label="Photo of rippling sea water"></div>
    <div class="brand-disc">Harbor Helm<br>Boat Training</div>
    <h1 class="holder-name">DANA R. WHITLOCK</h1>
    <p class="holder-title">USCG Licensed Captain<br>Certified Instructor</p>
    <div class="phone-pill">TEXT (555)014-2290</div>
    <p class="contact-line contact-line--email">service@helmready.com</p>
    <p class="contact-line contact-line--web">www.HelmReady.com</p>
  </section>

  <section class="card card--back">
    <div class="back-band"></div>
    <div class="sea-photo" role="img" aria-label="Photo of a white motorboat cruising on sparkling water"></div>
    <div class="brand-disc">Harbor Helm<br>Boat Training</div>
    <p class="band-web">www.HelmReady.com</p>
    <ul class="service-grid">
      <li class="service service--silver">Hand-On<br>Boat<br>Training</li>
      <li class="service service--accent">Indroduction<br>to Power<br>Boating</li>
      <li class="service service--silver">Precision<br>Docking &amp;<br>Boat Handling</li>
      <li class="service service--accent">Open Water<br>Boat Handling</li>
      <li class="service service--accent">Island<br>Anchoring</li>
      <li class="service service--silver">Open Water<br>Advanced<br>Maneuvers</li>
      <li class="service service--accent">Coastal<br>Navigation</li>
      <li class="service service--silver">Captaining<br>/ Piloting<br>Service for<br>Your Outings</li>
    </ul>
  </section>
</body>
</html>
```